Business card design for upmarket Home Technology design and Installation company

Hello designers, we need a great business card designed.
We need it to convey high tech, and also sophistication .
We work with some of the most affluent people in the world building them home technology systems, and A/V entertainment systems.

Services offered include the following:
Design, sales, installation, and maintenance of

*Home Automation systems
*Distributed / Multi-Room Audio and Video
*High Performance Networks & WiFi
* Lighting and Shade Control
*Home cinema
*Security and CCTV Systems

I have included a copy of our logo to use for your design efforts.

Target Market(s)

Upmarket clients with multi million euro villas.

Industry/Entity Type

Home technology

Contact Information for Business Card

NAME: Derek Halloran ADDRESS: Plaza Brisa Local 42, Port Andratx, 07392 PHONE: +34-602-518-794 EMAIL: DHalloran@VELTRAsmarthomes.com WEB: www.veltrasmarthomes.com

Requirements
Must have
• Our Logo, and our tagline

```html
<!DOCTYPE html>
<html lang="en">
<head>
<meta charset="utf-8">
<title>VELTRA Business Card</title>
<link href="https://fonts.googleapis.com/css2?family=Figtree:wght@300;400;800&display=swap" rel="stylesheet">
<style>
  :root {
    --stage: #d0d0d0;
    --card-dark: #141414;
    --pattern-tone: #2a2a2a;
    --card-light: #ffffff;
    --ink: #1c1c1c;
    --ink-soft: #2b2b2b;
    --on-dark: #ffffff;
  }
  * { margin: 0; padding: 0; box-sizing: border-box; }
  html, body {
    width: 1200px;
    height: 1000px;
    overflow: hidden;
    background: var(--stage);
    font-family: "Figtree", sans-serif;
  }
  .canvas { position: relative; width: 1200px; height: 1000px; }

  .card {
    position: absolute;
    left: 262px;
    width: 678px;
    height: 388px;
    border-radius: 26px;
    overflow: hidden;
  }

  /* Front: dark side */
  .card--front { top: 71px; background: var(--card-dark); }
  .front-pattern {
    position: absolute;
    inset: 0;
    background: radial-gradient(circle at 40% 40%, var(--pattern-tone), var(--card-dark) 85%);
  }
  .brand-mark--front {
    position: absolute;
    left: 703px; top: 266px;
    transform: translateX(-50%);
    left: 503px;
    display: flex;
    flex-direction: column;
    align-items: center;
    gap: 12px;
  }
  .brand-dot--front {
    width: 56px; height: 56px;
    border-radius: 50%;
    background: var(--on-dark);
  }
  .brand-name--front {
    font-weight: 400;
    font-size: 19px;
    letter-spacing: 3px;
    color: var(--on-dark);
  }

  /* Back: contact side */
  .card--back { top: 500px; background: var(--card-light); color: var(--ink); }
  .contact-list {
    position: absolute;
    left: 26px; top: 27px;
    list-style: none;
    font-weight: 300;
    font-size: 15px;
    line-height: 22px;
    color: var(--ink-soft);
  }
  .brand-mark--back {
    position: absolute;
    left: 588px; top: 28px;
    transform: translateX(-50%);
    display: flex;
    flex-direction: column;
    align-items: center;
    gap: 22px;
  }
  .brand-dot--back {
    width: 80px; height: 80px;
    border-radius: 50%;
    background: var(--ink);
  }
  .brand-name--back {
    font-weight: 400;
    font-size: 25px;
    letter-spacing: 4px;
    color: var(--ink);
  }
  .name-rule {
    position: absolute;
    left: 24px; top: 244px;
    width: 215px; height: 3px;
    background: var(--ink);
  }
  .holder-name {
    position: absolute;
    left: 24px; top: 260px;
    font-weight: 800;
    font-size: 54px;
    line-height: 54px;
    letter-spacing: 0.5px;
    text-transform: uppercase;
    color: var(--ink);
  }
</style>
</head>
<body>
<main class="canvas">
  <section class="card card--front">
    <div class="front-pattern" role="img" aria-label="Repeating grey brand-symbol pattern on black"></div>
    <div class="brand-mark brand-mark--front">
      <span class="brand-dot brand-dot--front"></span>
      <span class="brand-name brand-name--front">VELTRA</span>
    </div>
  </section>

  <section class="card card--back">
    <ul class="contact-list">
      <li>Phone: +34-602-518-794</li>
      <li>Email: dhalloran@veltrasmarthomes.com</li>
      <li>Website: www.veltrasmarthomes.com</li>
      <li>Address: Plaza Brisa, Local 42, 07392 Port d'Andratx,</li>
    </ul>
    <div class="brand-mark brand-mark--back">
      <span class="brand-dot brand-dot--back"></span>
      <span class="brand-name brand-name--back">VELTRA</span>
    </div>
    <div class="name-rule"></div>
    <h1 class="holder-name">Derek<br>Halloran</h1>
  </section>
</main>
</body>
</html>
```